Book cover for the book Where the Lantern Hums Before the Morning

I need a book cover for a book that explains that the mind, or consciousness, is the basis of reality. We live in a dream. This mind is all that exists. We have experiences in this dream. They are all in the mind. I see a tree, but the tree isn't outside in the world. It is an experience of sight wholly in the mind. The cover must not have brains. The mind is not in the brain. The brain is in the mind. We, as part of the universal intelligence, are creating this dream reality moment by moment. The cover doesn't have to show a mind creating a landscape, but that is one approach. It just has to be exciting and enticing. The big bang is really a big thought. I found a fascinating graphic I've attached as just an example. I also attach a page that I made that is dull just go give another approach. I want something much better.

```html
<!DOCTYPE html>
<html lang="en">
<head>
<meta charset="utf-8">
<title>Where the Lantern Hums Before the Morning — Book Cover</title>
<link rel="stylesheet" href="https://fonts.googleapis.com/css2?family=Orbitron:wght@400;500;700&family=Saira+Semi+Condensed:wght@500&display=swap">
<style>
  :root {
    --paper: #ffffff;
    --ink-teal: #1e7f8a;
    --sphere-light: #d6f6f3;
    --sphere-mid: #8fe0da;
    --sphere-deep: #5cc6c2;
    --spray: #6fd3cd;
  }
  html, body {
    margin: 0;
    padding: 0;
    overflow: hidden;
    background: var(--paper);
  }
  .cover {
    position: relative;
    width: 873px;
    height: 1200px;
    background: var(--paper);
    overflow: hidden;
  }
  .cover__art {
    position: absolute;
    inset: 0;
    width: 873px;
    height: 1200px;
  }
  .title-line {
    fill: var(--ink-teal);
    font-family: "Orbitron", sans-serif;
  }
  .title-line--small { font-size: 36px; font-weight: 400; }
  .title-line--joiner { font-size: 34px; font-weight: 400; }
  .title-line--hero { font-size: 128px; font-weight: 700; }
  .title-line--wide { font-size: 60px; font-weight: 500; }
  .cover__author {
    position: absolute;
    left: 0;
    right: 0;
    top: 1100px;
    margin: 0;
    padding-left: 5px;
    text-align: center;
    color: var(--ink-teal);
    font-family: "Saira Semi Condensed", sans-serif;
    font-weight: 500;
    font-size: 33px;
    letter-spacing: 0.5px;
  }
</style>
</head>
<body>
<main class="cover">
  <svg class="cover__art" viewBox="0 0 873 1200" xmlns="http://www.w3.org/2000/svg">
    <defs>
      <radialGradient id="sphere-fill" cx="45%" cy="40%" r="60%">
        <stop offset="0" stop-color="var(--sphere-light)"/>
        <stop offset="0.55" stop-color="var(--sphere-mid)"/>
        <stop offset="1" stop-color="var(--sphere-deep)"/>
      </radialGradient>
      <linearGradient id="spray-fill" x1="0" y1="0" x2="1" y2="1">
        <stop offset="0" stop-color="var(--spray)" stop-opacity="0.75"/>
        <stop offset="1" stop-color="var(--sphere-light)" stop-opacity="0.2"/>
      </linearGradient>
      <filter id="soft-edge" x="-30%" y="-30%" width="160%" height="160%">
        <feGaussianBlur stdDeviation="18"/>
      </filter>
    </defs>

    <g class="sphere-artwork" role="img" aria-label="Turquoise water sphere bursting into spray, droplets scattering to the upper left and lower right">
      <ellipse cx="240" cy="320" rx="110" ry="160" transform="rotate(-35 240 320)" fill="url(#spray-fill)" filter="url(#soft-edge)"/>
      <ellipse cx="640" cy="900" rx="120" ry="230" transform="rotate(-25 640 900)" fill="url(#spray-fill)" filter="url(#soft-edge)"/>
      <circle cx="405" cy="613" r="248" fill="url(#sphere-fill)"/>
    </g>

    <g class="cover__title" aria-label="Where the Lantern Hums Before the Morning">
      <text class="title-line title-line--small" x="205" y="509" textLength="444" lengthAdjust="spacingAndGlyphs">WHERE THE LANTERN</text>
      <text class="title-line title-line--joiner" x="378" y="549" textLength="100" lengthAdjust="spacingAndGlyphs">HUMS</text>
      <text class="title-line title-line--hero" x="205" y="660" textLength="446" lengthAdjust="spacingAndGlyphs">BEFORE</text>
      <text class="title-line title-line--joiner" x="378" y="698" textLength="100" lengthAdjust="spacingAndGlyphs">THE</text>
      <text class="title-line title-line--wide" x="126" y="762" textLength="597" lengthAdjust="spacing">MORNING</text>
    </g>
  </svg>

  <p class="cover__author">R ELDEN MARSH, PhD</p>
</main>
</body>
</html>
```